Kestrel Electrical Business Card

We need a business card design for our family-run electrical contracting business based in Western Australia called 'Kestrel Electrical'. We provide electrical services including residential, commercial and industrial. We aim for individual business cards to be made for all of our employees. We already have a company logo, which we require to be featured on the design. We would like simple, sleek and vibrant designs, which incorporate our logo and represent our business. We do not want anything involving too many graphics/images. We like the colours red, black, white and all shades of grey. The final design should communicate professionalism and trustworthiness.
We require the following contact information:
Name- Owen Strickland
EC 5809
Mobile number- 0455 918 302
Fax number (including area code)- (08) 9640 2718
Email adress- name@kestrelelectrical.example
Electrical
- ITC Handel Bold

```html
<!DOCTYPE html>
<html lang="en">
<head>
<meta charset="utf-8">
<title>Kestrel Electrical Business Card</title>
<link href="https://fonts.googleapis.com/css2?family=Exo+2:wght@400;700&family=Oswald:wght@500&display=swap" rel="stylesheet">
<style>
  :root {
    --stage: #1d1d1f;
    --card-black: #0c0c0c;
    --card-white: #ffffff;
    --brand-red: #e3221c;
    --ink: #1a1a1a;
    --grey-soft: #d9d9d9;
  }
  * { box-sizing: border-box; margin: 0; padding: 0; }
  html, body { width: 1200px; height: 863px; overflow: hidden; }
  body {
    background: var(--stage);
    font-family: "Exo 2", "Segoe UI", sans-serif;
    position: relative;
  }
  .card {
    position: absolute;
    width: 540px;
    height: 309px;
    top: 277px;
    overflow: hidden;
    box-shadow: 0 18px 40px rgba(0,0,0,.55);
  }

  /* Front */
  .card--front { left: 40px; background: var(--card-black); }
  .front-panel {
    position: absolute;
    left: 112px; top: 56px;
    width: 400px; height: 176px;
    background: var(--card-white);
    display: flex; align-items: center; justify-content: center;
  }
  .front-web {
    position: absolute;
    left: 112px; width: 400px; top: 252px;
    text-align: center;
    color: var(--card-white);
    font-size: 11px;
    letter-spacing: .04em;
  }

  /* Wordmark */
  .wordmark { display: flex; align-items: center; gap: 12px; }
  .wordmark-square { width: 34px; height: 34px; background: var(--brand-red); flex: none; }
  .wordmark-name {
    font-weight: 700;
    color: var(--ink);
    text-transform: uppercase;
    line-height: 1;
  }
  .wordmark-name span { display: block; }
  .wordmark-name .top { font-size: 34px; letter-spacing: .01em; }
  .wordmark-name .bottom { font-size: 13px; letter-spacing: .42em; margin-top: 4px; }

  /* Back */
  .card--back { left: 620px; background: var(--card-white); }
  .back-logo {
    position: absolute;
    left: 12px; top: 172px;
    width: 250px;
    display: flex; justify-content: center;
  }
  .back-logo .wordmark-name .top { font-size: 27px; }
  .back-logo .wordmark-name .bottom { font-size: 10.5px; letter-spacing: .38em; }
  .back-logo .wordmark-square { width: 27px; height: 27px; }
  .back-dark {
    position: absolute; inset: 0;
    background: var(--card-black);
    clip-path: polygon(47% 0, 100% 0, 100% 100%, 54% 100%, 47% 32%);
  }
  .name-band {
    position: absolute;
    left: 214px; top: 38px;
    width: 326px; height: 64px;
    background: var(--brand-red);
    clip-path: polygon(5% 0, 100% 0, 100% 100%, 0 100%);
    padding: 8px 0 0 58px;
    color: var(--card-white);
  }
  .person-name {
    font-family: "Oswald", "Arial Narrow", sans-serif;
    font-weight: 500;
    font-size: 25px;
    line-height: 1.1;
    text-transform: uppercase;
  }
  .person-role {
    font-size: 9px;
    letter-spacing: .14em;
    text-transform: uppercase;
  }
  .contact-list { position: absolute; left: 258px; top: 126px; list-style: none; }
  .contact-item { display: flex; align-items: center; gap: 14px; height: 54px; }
  .contact-icon {
    width: 28px; height: 28px; border-radius: 50%;
    background: var(--card-white);
    display: flex; align-items: center; justify-content: center;
    flex: none;
  }
  .contact-text {
    color: var(--card-white);
    font-size: 12px;
    line-height: 1.3;
    letter-spacing: .02em;
  }
</style>
</head>
<body>

  <section class="card card--front" aria-label="Business card front">
    <div class="front-panel">
      <div class="wordmark">
        <div class="wordmark-square"></div>
        <div class="wordmark-name"><span class="top">Kestrel</span><span class="bottom">Electrical</span></div>
      </div>
    </div>
    <p class="front-web">www.kestrelelectrical.example</p>
  </section>

  <section class="card card--back" aria-label="Business card back">
    <div class="back-dark"></div>
    <div class="back-logo">
      <div class="wordmark">
        <div class="wordmark-square"></div>
        <div class="wordmark-name"><span class="top">Kestrel</span><span class="bottom">Electrical</span></div>
      </div>
    </div>
    <div class="name-band">
      <h1 class="person-name">Owen Strickland</h1>
      <p class="person-role">General Manager</p>
    </div>
    <ul class="contact-list">
      <li class="contact-item">
        <span class="contact-icon">
          <svg width="14" height="16" viewBox="0 0 14 16"><path d="M7 0a6 6 0 0 0-6 6c0 4.5 6 10 6 10s6-5.5 6-10a6 6 0 0 0-6-6zm0 8.4A2.4 2.4 0 1 1 7 3.6a2.4 2.4 0 0 1 0 4.8z" fill="#0c0c0c"/></svg>
        </span>
        <p class="contact-text">14 Harbour View Road,<br>Unit 3, Perth WA</p>
      </li>
      <li class="contact-item">
        <span class="contact-icon">
          <svg width="16" height="16" viewBox="0 0 16 16"><path d="M3.5 1l2.6 3.2-1.5 1.8c.9 2 2.5 3.6 4.4 4.5l1.8-1.5L14 11.6 12.6 14C6.5 13.6 2.4 9.5 2 3.4z" fill="#0c0c0c"/></svg>
        </span>
        <p class="contact-text">0455 918 302<br>(08) 9640 2718</p>
      </li>
      <li class="contact-item">
        <span class="contact-icon">
          <svg width="16" height="16" viewBox="0 0 16 16" fill="none" stroke="#0c0c0c" stroke-width="1.3"><circle cx="8" cy="8" r="6.5"/><ellipse cx="8" cy="8" rx="3" ry="6.5"/><path d="M1.5 8h13M2.6 4.5h10.8M2.6 11.5h10.8"/></svg>
        </span>
        <p class="contact-text">name@kestrelelectrical.example<br>www.kestrelelectrical.example</p>
      </li>
    </ul>
  </section>

</body>
</html>
```